Creative, Innovative PowerPoint Sales Deck Refresh needed

We are a technology firm in the Dallas, TX area and we need the powerpoint presentation used for our sales calls refreshed. This presentation is used in one of the first meetings we have with potential clients, so we want to make a memorable and positive impact - we want something that sets us apart from everyone else. We need 8 master slide templates created for our sales deck and a series of slides within the example sales deck need to be completely refreshed (slides 31-37 and 43 in the sample ppt file) We want a sales deck that is modern, innovative, creative, memorable and whimsical - NOT a typical boring "business" design. Colors should match or compliment the colors used in our logo. The logo in the footer of the attached sample ppt is old - it should be replaced with the newer logo attached. Please take a look at our website to get an idea of our culture and aesthetic www.quorbinlab.com
Updates

Project Deadline Extended
Reason: We have received several designs we like and we want our entire team to have time to give them full consideration before making a decision.

Target Market(s)

Business executives

Industry/Entity Type

Information Technology

Font styles to use
Sans Serif

Requirements
Must have
• Our logo and LedgerWave logo in footer
• Master Slide Templates
• Rework / redesign of slides 31-37 and 43
Nice to have
• We use Raleway font in a lot of our materials

```html
<!DOCTYPE html>
<html lang="en">
<head>
<meta charset="utf-8">
<title>Phase One Methodology</title>
<link href="https://fonts.googleapis.com/css2?family=Source+Sans+3:wght@300;400;600;700&display=swap" rel="stylesheet">
<style>
  :root {
    --bg: #ffffff;
    --ink: #1c1c1c;
    --list-ink: #111111;
    --bullet-blue: #3a63ad;
    --green-1: #82c341;
    --green-2: #97cd5e;
    --green-3: #acd77d;
    --green-4: #bfe09b;
    --green-5: #cde6b0;
    --band-dark: #6a6b6e;
    --band-light: #c8c9cb;
    --corner-dark: #5b5c5f;
    --corner-light: #cfd0d2;
    --photo-deep: #1e2a1e;
    --photo-mid: #6f8a72;
    --photo-pale: #d9e6da;
    --mark-navy: #1b3c6e;
  }
  * { margin: 0; padding: 0; box-sizing: border-box; }
  html, body { width: 1200px; height: 750px; overflow: hidden; background: var(--bg); }
  body { font-family: "Source Sans 3", sans-serif; color: var(--ink); }

  .slide { position: relative; width: 1200px; height: 750px; overflow: hidden; background: var(--bg); }
  .slide-art { position: absolute; inset: 0; width: 1200px; height: 750px; }

  .slide-title {
    position: absolute; left: 404px; top: 88px;
    font-size: 53px; font-weight: 300; line-height: 1; letter-spacing: 0.2px;
  }

  .phase-steps { position: absolute; left: 403px; top: 263px; width: 520px; height: 100px; }
  .phase-step {
    position: absolute; top: 0; width: 100px; height: 100px; border-radius: 50%;
    display: flex; align-items: center; justify-content: center; text-align: center;
    color: #fff; font-weight: 700; font-size: 17px; line-height: 1.2;
  }
  .phase-step:nth-child(1) { left: 0;    background: var(--green-1); z-index: 5; }
  .phase-step:nth-child(2) { left: 91px; background: var(--green-2); z-index: 4; }
  .phase-step:nth-child(3) { left: 182px; background: var(--green-3); z-index: 3; }
  .phase-step:nth-child(4) { left: 273px; background: var(--green-4); z-index: 2; }
  .phase-step:nth-child(5) { left: 364px; background: var(--green-5); z-index: 1; }

  .task-list { position: absolute; left: 400px; top: 396px; list-style: none; }
  .task-list li {
    position: relative; padding-left: 32px; height: 33px; line-height: 24px;
    font-size: 17px; font-weight: 400; color: var(--list-ink);
  }
  .task-list li::before {
    content: ""; position: absolute; left: 0; top: 2px; width: 20px; height: 20px;
    border: 2.5px solid var(--bullet-blue); border-radius: 50%;
  }

  .brand-footer { position: absolute; left: 0; top: 0; width: 1200px; height: 750px; pointer-events: none; }
  .brand-dot { position: absolute; left: 414px; top: 640px; width: 56px; height: 56px; border-radius: 50%; background: var(--green-1); }
  .brand-divider { position: absolute; left: 498px; top: 637px; width: 1.5px; height: 62px; background: var(--ink); }
  .brand-name {
    position: absolute; left: 521px; top: 650px;
    font-size: 26px; font-weight: 400; color: var(--ink); letter-spacing: -0.3px;
  }
  .partner-square { position: absolute; left: 848px; top: 643px; width: 52px; height: 52px; background: var(--mark-navy); }
  .partner-name {
    position: absolute; left: 914px; top: 645px;
    font-size: 38px; font-weight: 600; color: var(--ink); letter-spacing: 1px; line-height: 1.2;
  }
</style>
</head>
<body>
<main class="slide">
  <svg class="slide-art" viewBox="0 0 1280 800" preserveAspectRatio="none" aria-hidden="false">
    <defs>
      <linearGradient id="photoTone" x1="0" y1="0" x2="1" y2="1">
        <stop offset="0" stop-color="var(--photo-deep)"/>
        <stop offset="0.45" stop-color="var(--photo-mid)"/>
        <stop offset="1" stop-color="var(--photo-pale)"/>
      </linearGradient>
    </defs>
    <g role="img" aria-label="Photo of business people standing at a meeting table with papers and a laptop">
      <polygon points="0,0 412,0 0,700" fill="url(#photoTone)"/>
    </g>
    <polygon class="band-light" points="295,235 332,258 58,684 42,626" fill="var(--band-light)"/>
    <polygon class="band-dark" points="213,290 228,340 0,702 0,640" fill="var(--band-dark)"/>
    <polygon class="corner-light" points="1215,0 1268,0 1205,157 1178,62" fill="var(--corner-light)"/>
    <polygon class="corner-dark" points="1262,0 1281,0 1281,66 1240,135 1224,86" fill="var(--corner-dark)"/>
  </svg>

  <h1 class="slide-title">Phase One Methodology</h1>

  <div class="phase-steps">
    <div class="phase-step">Project<br>initiation</div>
    <div class="phase-step"></div>
    <div class="phase-step"></div>
    <div class="phase-step"></div>
    <div class="phase-step"></div>
  </div>

  <ul class="task-list">
    <li>Project Initiation</li>
    <li>Conduct Kickoff Meeting</li>
    <li>Finalize and Publish Project Schedule</li>
    <li>Requirements Definition and Design</li>
    <li>Requirements Traceability Matrix (RTM) Signoff</li>
  </ul>

  <footer class="brand-footer">
    <span class="brand-dot"></span>
    <span class="brand-divider"></span>
    <span class="brand-name">quorbinlab</span>
    <span class="partner-square"></span>
    <span class="partner-name">LEDGERWAVE</span>
  </footer>
</main>
</body>
</html>
```